2 banner Designs

I have a trade show in Vegas and I want you to design 2 banners that are Graphic size: 33.5" (W) x 80.5" (H). The banners are standing in the booth.

I am looking for a luxury modern feel for the banners. The banners are going to be important to attract customers in.

I am showing latex foam pillows and latex mattress. The company is called Verdant Rest. Please use any photos from our website.

https://www.lumivaslee.net/verdantrest

Banner 1

Introducing our Verdant Rest mattress, a perfect harmony of luxurious organic cushioning and an advanced internal, zoned pressure-point support system.

Experience unparalleled back support and remarkable durability, all in one exceptional sleep solution.

Verdant Rest Mattress

HVRA-certified organic cotton
HVRA-certified organic wool
2 “ HVLA-certified organic latex
8” Pocket Coils
1’’ HVLA-certified organic latex

Banner 2

Verdant Rest Pillows

We developed a customizable pillow with the perfect amount of comfort and support.

Our New Latex pillow has an adjustable fill with 90% Natural Latex and 10% Traceable Wool.  Our pillow cover is made from HVRA-certified organic cotton.

FILE REQUIREMENTS
We can take the file in the following file formats:

Single Page PDF (Preferred)
JPG (Preferred)
PSD – Please flatten file
EPS – Please embed all images. Outline all fonts and strokes.
Ai – Please embed all images. Outline all fonts and strokes.
Don't Include Crop Marks or Bleed

Artwork at either full scale, 1/2 scale or 1/10 scale that is fine. Just make sure that when the file is being set up the DPI is compensated according to the scale.

Full Scale – 150 DPI
1/2 Scale – 300 DPI
1/10 Scale – 450 DPI
***Remove EVERYTHING from your file that you do not want printed on the final product - especially hidden layers and template guidelines.

- Flatten all Objects/Gradients/Swatches/Symbols/Special Effects/Transparencies
- Outline all text
- Flattened PDF (Single Page) or JPEG file types only
- Remove all crop marks/bleed otherwise they will be printed
- File must be the same exact size as what is ordered (exception is Gallery wrap Fold Edge and Products with templates)
- CMYK only (we do not print Pantone/5th/Spot/RGB)
- 150 dpi
- If using a template, the file uploaded to our site should match the exact "template size" (different than "graphic size").
- Do not scale template files, just flatten them and save at 150 dpi
- Files over 200" can be scaled
- Under 300 mb for upload

- Make sure all objects are embedded and flattened (we do not print Non-Native Art).
- If the file is made in Indesign, please flatten the file in Illustrator or Photoshop and export to a JPEG ONLY as we don't recommend using Indesign at our facility.

- If using Compound Paths to create transparencies/shapes, please completely rasterize or flatten them into the file or they may print incorrectly.

- We do not have specific measurements for Panel jobs. If you are printing in Panels, please make sure you are providing a minimum of 1" overlay in your files.

Please make sure that your file is in CMYK format for print production with no bleed. It is not required.

```html
<!DOCTYPE html>
<html lang="en">
<head>
<meta charset="utf-8">
<title>Verdant Rest – Trade Show Banners</title>
<link href="https://fonts.googleapis.com/css2?family=Cinzel:wght@400;600;700&display=swap" rel="stylesheet">
<style>
  :root {
    --canvas: #e6e6e6;
    --paper: #ffffff;
    --leaf: #66841c;
    --ink: #000000;
    --text-light: #ffffff;
  }
  * { margin: 0; padding: 0; box-sizing: border-box; }
  html, body { width: 1043px; height: 1200px; overflow: hidden; background: var(--canvas); }
  body { position: relative; font-family: "Cinzel", "Times New Roman", serif; color: var(--text-light); }

  .banner {
    position: absolute;
    width: 465px; height: 1116px;
    background: var(--paper);
    border: 1px solid #5f7a1a;
    overflow: hidden;
  }
  .banner--mattress { left: 45px; top: 45px; }
  .banner--pillow { left: 548px; top: 51px; }

  .banner__art { position: absolute; inset: 0; width: 100%; height: 100%; }

  .brand {
    position: absolute; left: 0; right: 0; top: 120px;
    text-align: center; color: var(--leaf);
    font-weight: 400; font-size: 34px; letter-spacing: 1px; line-height: 1;
  }

  .copy { position: absolute; left: 0; right: 0; text-align: center; }

  .mattress-intro { top: 612px; font-size: 17px; line-height: 23.5px; letter-spacing: .3px; }
  .mattress-intro .lead { font-size: 20px; }
  .mattress-detail { top: 768px; font-size: 14.5px; line-height: 21.5px; letter-spacing: .4px; }
  .mattress-title { top: 842px; font-size: 23px; font-weight: 700; letter-spacing: .3px; }
  .spec-list { top: 885px; left: 40px; right: 0; text-align: left; list-style: none; font-size: 17px; line-height: 25.6px; }
  .spec-list li::before { content: "·"; font-size: 10px; margin-right: 6px; vertical-align: middle; }

  .pillow-title { top: 613px; font-size: 34px; line-height: 43px; font-weight: 400; }
  .pillow-lead { top: 724px; font-size: 19px; line-height: 33.5px; letter-spacing: .3px; }
  .pillow-fill { top: 843px; font-size: 17px; line-height: 25px; letter-spacing: .3px; }
  .pillow-cover { top: 943px; font-size: 19.5px; line-height: 24px; letter-spacing: .2px; }

  .contact { position: absolute; left: 0; right: 0; top: 1054px; text-align: center; font-weight: 700; }
  .contact__address { font-size: 17.5px; line-height: 22px; }
  .contact__phone { font-size: 25px; line-height: 30px; }
</style>
</head>
<body>

<section class="banner banner--mattress">
  <svg class="banner__art" viewBox="0 0 668 1605" preserveAspectRatio="none">
    <defs>
      <linearGradient id="mattressPhotoTone" x1="0" y1="0" x2="1" y2="1">
        <stop offset="0" stop-color="#eae4da"/>
        <stop offset=".5" stop-color="#d9c6ae"/>
        <stop offset="1" stop-color="#f1ede6"/>
      </linearGradient>
    </defs>
    <rect y="715" width="668" height="890" fill="var(--leaf)"/>
    <polygon points="334,253 668,415 668,715 334,877 0,715 0,415" fill="var(--ink)"/>
    <polygon points="334,280 645,430 645,705 334,852 23,705 23,430" fill="url(#mattressPhotoTone)" role="img" aria-label="Photo of a smiling woman hugging a latex pillow on a bed"/>
    <rect y="1474" width="668" height="6" fill="var(--ink)"/>
  </svg>

  <div class="brand">VERDANT REST</div>

  <p class="copy mattress-intro">Introducing our<br><span class="lead">Verdant Rest mattress,</span><br>a perfect harmony of luxurious<br>organic cushioning and an<br>advanced internal, zoned<br>pressure-point support system.</p>
  <p class="copy mattress-detail">Experience unparalleled back support<br>and remarkable durability, all in one<br>exceptional sleep solution.</p>
  <h2 class="copy mattress-title">Verdant Rest Mattress</h2>
  <ul class="copy spec-list">
    <li>HVRA-certified organic cotton</li>
    <li>HVRA-certified organic wool</li>
    <li>2 “ HVLA-certified organic latex</li>
    <li>8” Pocket Coils</li>
    <li>1” HVLA-certified organic latex</li>
  </ul>

  <div class="contact">
    <div class="contact__address">412 Alder Street Fairmont, CA 90210</div>
    <div class="contact__phone">555.204.3187</div>
  </div>
</section>

<section class="banner banner--pillow">
  <svg class="banner__art" viewBox="0 0 668 1605" preserveAspectRatio="none">
    <defs>
      <linearGradient id="pillowPhotoTone" x1="0" y1="0" x2="0" y2="1">
        <stop offset="0" stop-color="#b4b1ad"/>
        <stop offset=".45" stop-color="#e4e1da"/>
        <stop offset="1" stop-color="#a8a5a1"/>
      </linearGradient>
    </defs>
    <rect y="707" width="668" height="898" fill="var(--leaf)"/>
    <polygon points="334,245 668,402 668,707 334,868 0,707 0,402" fill="var(--ink)"/>
    <polygon points="334,272 645,417 645,697 334,843 23,697 23,417" fill="url(#pillowPhotoTone)" role="img" aria-label="Photo of a quilted latex mattress topper on a bed"/>
    <line x1="34" y1="1337" x2="634" y2="1337" stroke="#2f3d0c" stroke-width="1.5"/>
    <rect y="1474" width="668" height="6" fill="var(--ink)"/>
  </svg>

  <div class="brand">VERDANT REST</div>

  <h2 class="copy pillow-title">Verdant Rest<br>Pillows</h2>
  <p class="copy pillow-lead">we developed a customizable<br>pillow with the perfect amount<br>of comfort and support.</p>
  <p class="copy pillow-fill">Our New Latex pillow has an<br>adjustable fill with 90% Natural<br>Latex and 10% Traceable Wool.</p>
  <p class="copy pillow-cover">our pillow cover is made from<br>HVRA-certified organic cotton.</p>

  <div class="contact">
    <div class="contact__address">412 Alder Street Fairmont, CA 90210</div>
    <div class="contact__phone">555.204.3187</div>
  </div>
</section>

</body>
</html>
```